High Quality Business card for Property Management Agency - Super Classy and professional design

High Quality Business card design.

We need a business card designed for our Property Management Agency.
We are located on Sydney's Northern Beaches and manage beautiful properties along the beach and harbor.
We need a design that oozes modern, classy and professional.
I would like it to be double sided with contact details and logo on the front and just the logo on the back.

I need a print ready PDF version of the file as well as an editable photoshop (PSD) version of the file.

Logo and information details attached.

Target Market(s)

Property owners/investors, Male and Female Aged 28-65

Industry/Entity Type

Real Estate

Contact Information for Business Card

Tom Carrick
Tel: 0467 239 018
Email: tom@harvestlaneestates.com.au
Website: www.harvestlaneestates.com.au
Address: Level 2, 17 Wattlecourt Rd, Dunmarra NSW 2187

Font styles to use
Sans Serif

Requirements
Must have
• - Logo front and back
• - Business card details listed above and attached
• - Colour
Nice to have
• Sleek and professional

```html
<!DOCTYPE html>
<html lang="en">
<head>
<meta charset="utf-8">
<title>Harvest Lane Estates – Business Card</title>
<link rel="stylesheet" href="https://fonts.googleapis.com/css2?family=Open+Sans:wght@400;600;700&display=swap">
<style>
  :root {
    --backdrop: #dfe2e8;
    --card-white: #ffffff;
    --card-black: #141515;
    --teal: #2a9aa3;
    --teal-deep: #1f7f88;
    --ink: #1b1b1b;
    --rule: #333333;
  }
  * { box-sizing: border-box; margin: 0; padding: 0; }
  html, body {
    width: 1200px;
    height: 797px;
    overflow: hidden;
    background: var(--backdrop);
    font-family: "Open Sans", sans-serif;
    color: var(--ink);
  }
  .sheet {
    position: relative;
    width: 1200px;
    height: 797px;
    display: flex;
    align-items: center;
    justify-content: center;
    gap: 60px;
  }
  .card {
    position: relative;
    width: 520px;
    height: 297px;
    overflow: hidden;
    box-shadow: 0 6px 18px rgba(40, 50, 70, 0.18);
  }

  /* Back side */
  .card--back {
    background: var(--card-black);
    display: flex;
    align-items: center;
    justify-content: center;
  }
  .card--back .brand { color: var(--card-white); font-size: 30px; }
  .card--back .brand__dot { background: var(--teal); }

  /* Brand name */
  .brand {
    display: flex;
    align-items: center;
    gap: 10px;
    font-weight: 600;
    letter-spacing: 0.5px;
    text-transform: uppercase;
    white-space: nowrap;
  }
  .brand__dot {
    width: 14px;
    height: 14px;
    border-radius: 50%;
    flex: none;
  }

  /* Front side */
  .card--front { background: var(--card-white); }
  .card--front .brand {
    position: absolute;
    top: 34px;
    right: 30px;
    font-size: 22px;
    color: var(--ink);
  }
  .card--front .brand__dot { background: var(--teal); }

  .holder {
    position: absolute;
    left: 30px;
    top: 118px;
    width: 460px;
    border-bottom: 1px solid var(--rule);
    padding-bottom: 4px;
  }
  .holder__name {
    font-size: 17px;
    font-weight: 700;
    color: var(--teal);
    line-height: 1.2;
  }
  .holder__role {
    font-size: 12.5px;
    line-height: 1.3;
  }

  .contacts {
    position: absolute;
    left: 30px;
    top: 172px;
    list-style: none;
    font-size: 12px;
    line-height: 19px;
  }
  .contacts__item { display: flex; align-items: center; gap: 7px; }
  .contacts__icon { width: 13px; height: 13px; flex: none; }

  .address {
    position: absolute;
    right: 30px;
    bottom: 34px;
    font-size: 11.5px;
    line-height: 16px;
    text-align: right;
    font-style: normal;
  }

  .card__band {
    position: absolute;
    left: 0;
    right: 0;
    bottom: 0;
    height: 14px;
    background: linear-gradient(90deg, var(--teal-deep), var(--teal));
  }
</style>
</head>
<body>
<main class="sheet">

  <section class="card card--back" aria-label="Card back">
    <div class="brand"><span class="brand__dot"></span>Harvest Lane Estates</div>
  </section>

  <section class="card card--front" aria-label="Card front">
    <div class="brand"><span class="brand__dot"></span>Harvest Lane Estates</div>

    <div class="holder">
      <p class="holder__name">Tom Carrick</p>
      <p class="holder__role">Director/Property Manager</p>
    </div>

    <ul class="contacts">
      <li class="contacts__item">
        <svg class="contacts__icon" viewBox="0 0 16 16" aria-hidden="true">
          <circle cx="8" cy="8" r="8" fill="var(--teal)"/>
          <path d="M5 4.5c.6-.4 1.1-.2 1.4.4l.5 1c.2.5 0 .9-.4 1.1l-.3.2c.4 1 1.1 1.8 2.1 2.2l.2-.3c.3-.4.7-.5 1.1-.3l1 .5c.6.3.8.8.4 1.4-.6.9-1.6 1.1-2.6.6C6.6 10.5 5.3 9.1 4.6 7.3c-.4-1.1-.3-2.1.4-2.8z" fill="#fff"/>
        </svg>
        <span>0467 239 018</span>
      </li>
      <li class="contacts__item">
        <svg class="contacts__icon" viewBox="0 0 16 16" aria-hidden="true">
          <circle cx="8" cy="8" r="8" fill="var(--teal)"/>
          <rect x="4" y="5.2" width="8" height="5.6" fill="#fff"/>
          <path d="M4 5.4l4 3 4-3" fill="none" stroke="var(--teal)" stroke-width="0.9"/>
        </svg>
        <span>tom@harvestlaneestates.com.au</span>
      </li>
      <li class="contacts__item">
        <svg class="contacts__icon" viewBox="0 0 16 16" aria-hidden="true">
          <circle cx="8" cy="8" r="8" fill="var(--teal)"/>
          <g fill="none" stroke="#fff" stroke-width="0.9">
            <circle cx="8" cy="8" r="4.3"/>
            <ellipse cx="8" cy="8" rx="1.9" ry="4.3"/>
            <path d="M3.7 8h8.6M4.4 5.8h7.2M4.4 10.2h7.2"/>
          </g>
        </svg>
        <span>www.harvestlaneestates.com.au</span>
      </li>
    </ul>

    <address class="address">
      Level 2, 17 Wattlecourt Rd,<br>
      Dunmarra NSW 2187
    </address>

    <div class="card__band"></div>
  </section>

</main>
</body>
</html>
```